Real Estate Investor needs awesome business card design

I invest in real estate, focused on multi-family properties, and I need a business card to hand out to potential partners. I prefer simple, clean designs, but it needs to stand out, so I'd like there to be a bit of red in the design as well.

It should include this information:

Front
Dallin Pecksworth
Real Estate Investor
Direct phone: 502-867-3394
Email: dallinhpecksworth@quillmail.example
Headshot (Picture), I've uploaded a few, just pick the one you think looks best with your design. You can remove the background from the headshot image if it looks better.

Back
The back of the card's design should flow and be congruent with the front. On the back I want to put an inspirational quote or question. There will be different ones depending on the card, so I'll need the original file so I can edit it in the end.

For now, use “The Pessimist Sees Difficulty In Every Opportunity. The Optimist Sees The Opportunity In Every Difficulty.” -Barnaby Ellsworth

Target Market(s)

Investors

Industry/Entity Type

Real Estate

Contact Information for Business Card

Front
Dallin Pecksworth
Real Estate Investor

Back
The back of the card's design should flow and be congruent with the front. On the back I want to put an inspirational quote or question. There will be different ones depending on the card, so I'll need the original file so I can edit it in the end. I've uploaded some EXAMPLES of business cards with quotes on them. Don't copy but feel free to use them as inspiration.

The design will be printed on "ZIB sized" business cards
1039 x 697 pixels
with rounded corners

Font styles to use
Serif
Decorative
Script

Colors
ec1f27

Requirements
Must have
• Headshot, name, and other information in it.
• 1039 x 697 pixels
• Rounded corners
• Clean design that pops. I'm open to see any color background, including black.
• Headshots can be located here: https://www.filecrate.example/sh/8kd2wq7mzt31hvx/BBQTXP4ruf9LmQ0KhcvWx7b?dl=0
Nice to have
• It would be awesome if the design included a personal signature or monogram, but if not I'll get a personal logo developed later and the card redesigned if I think it needs it.
Should not have
• Cluttered design

```html
<!DOCTYPE html>
<html lang="en">
<head>
<meta charset="utf-8">
<title>Dallin Pecksworth – Business Card</title>
<link rel="stylesheet" href="https://fonts.googleapis.com/css2?family=Gelasio:ital,wght@0,400;0,700;1,700&display=swap">
<style>
  :root {
    --bg: #e9e6e2;
    --card-white: #ffffff;
    --card-black: #000000;
    --ink: #111111;
    --red: #ec1f27;
    --quote: #f2f2f2;
    --photo-light: #f3f4f6;
    --photo-mid: #c9b7a6;
    --photo-dark: #1d2433;
  }
  * { box-sizing: border-box; margin: 0; padding: 0; }
  html, body {
    width: 1200px; height: 942px; overflow: hidden;
    background: var(--bg);
    font-family: "Gelasio", Georgia, serif;
  }
  .canvas { position: relative; width: 1200px; height: 942px; }
  .card {
    position: absolute; left: 277px; width: 646px; height: 392px;
    border-radius: 16px; overflow: hidden;
    box-shadow: 0 6px 14px rgba(0,0,0,.25);
  }
  .card--front { top: 58px; background: var(--card-white); }
  .card--back { top: 478px; background: var(--card-black); }

  .headshot {
    position: absolute; right: 0; top: 0; width: 380px; height: 392px;
    background:
      radial-gradient(ellipse 90px 120px at 62% 45%, var(--photo-mid), transparent 75%),
      radial-gradient(ellipse 200px 110px at 62% 100%, var(--photo-dark), transparent 80%),
      linear-gradient(90deg, var(--card-white) 0%, var(--photo-light) 35%, var(--photo-light) 100%);
  }

  .contact {
    position: absolute; left: 20px; top: 152px; width: 310px;
    text-align: center; color: var(--ink);
  }
  .contact__name { color: var(--red); font-size: 27px; line-height: 1.1; font-weight: 400; }
  .contact__title { font-size: 16px; line-height: 1.3; }
  .contact__lines { margin-top: 12px; font-size: 15px; line-height: 1.4; }
  .contact__label { color: var(--red); }

  .quote {
    position: absolute; left: 0; right: 0; top: 168px;
    text-align: center; color: var(--quote);
    font-size: 17px; line-height: 24px;
  }
  .quote__author {
    display: block; color: var(--red);
    font-weight: 700; font-style: italic; text-transform: uppercase;
    font-size: 18px; line-height: 26px;
  }
</style>
</head>
<body>
<main class="canvas">
  <section class="card card--front">
    <div class="headshot" role="img" aria-label="Headshot photo of Dallin Pecksworth in a dark suit jacket and white shirt"></div>
    <div class="contact">
      <h1 class="contact__name">Dallin Pecksworth</h1>
      <p class="contact__title">Real Estate Investor</p>
      <p class="contact__lines">
        <span class="contact__label">P:</span> 502-867-3394<br>
        <span class="contact__label">E:</span> dallinhpecksworth@quillmail.example
      </p>
    </div>
  </section>

  <section class="card card--back">
    <blockquote class="quote">
      The Pessimist Sees Difficulty In Every Opportunity.<br>
      The Optimist Sees The Opportunity In Every Difficulty.
      <cite class="quote__author">Barnaby Ellsworth</cite>
    </blockquote>
  </section>
</main>
</body>
</html>
```